New Website for Crime Scene Cleaner required

I need someone to create a complete new website and can set up SEO for me through the Website Designer or a third party for me. I have Logo that i will upload shortly once finalized for the website. I have domain names already but will need to be registered by the winner(i can supply the details I have received from HostMarlo). I am looking for a website that stands out but is simple and elegant, easy to navigate and use yet not boring. Using information provided by me for wording to create it as a stand out website. in total i am looking at 5-7 pages (About/Home, Fire & Smoke Restoration, Water Restoration/Mould Remediation, Crime Scene Cleaners, Methamphetamine Remediation/ Testing Services, Hoarding & Squalor Cleaning, Contact Us/Testimonials)This will be a start to finish project. I would like assistance to have it set up user friendly on mobile devices etc or refer a third party who can assist. Must be able to provide ongoing support when required by myself if the successful winner (i understand this will be an additional fee if required in the future).
You will also require to assist me with the email set up for the website so that it is fully functional or provide a third party who can.
To gain some information about the business you can visit my old website at www.pelbrookcove.com.au and welcome to use some of the wording from there for your entry.
It's been 14yrs since i've had a website made from me so suggestions are welcome if not mentioned in the scope as I want the website to be great.

I have uploaded 2 Logo's and a 3D Logo will come through shortly.

Target Market(s)

People affected by a traumatic event in their lives needing assistance by professionals who are understanding and professionally trained

Coding

Coded - Design and coding required

Requirements
Must have
• *** Please note that correct wording for pages will only be supplied upon a successful winner for the finalization of the project.

I have domain names already but will need to be registered by the winner(i can supply the details I have received from HostMarlo).
Nice to have
• the feeling that we care because we do and that we are passionate for what we do.

```html
<!DOCTYPE html>
<html lang="en">
<head>
<meta charset="utf-8">
<title>Keystone Recovery Services</title>
<link href="https://fonts.googleapis.com/css2?family=Michroma&family=Roboto:ital,wght@0,400;0,500;0,700;1,500&display=swap" rel="stylesheet">
<style>
:root{
  --orange:#f37321;
  --orange-dark:#e0621a;
  --ink:#222;
  --text:#444;
  --white:#fff;
  --light:#f4f4f4;
  --footer:#232323;
}
*{box-sizing:border-box;margin:0;padding:0}
html,body{width:1200px;height:3673px;overflow:hidden}
body{font-family:'Roboto',sans-serif;color:var(--text);background:var(--white);position:relative}
.display{font-family:'Michroma',sans-serif;font-weight:400;color:var(--ink);letter-spacing:1px}
.abs{position:absolute}

/* header */
.header{top:0;left:0;width:1200px;height:107px}
.brand{left:88px;top:28px;display:flex;align-items:center;gap:10px}
.brand-mark{width:36px;height:36px;border-radius:50%;background:var(--orange)}
.brand-name{font-size:17px;font-weight:700;color:var(--orange);line-height:1.1;text-transform:uppercase}
.contact{display:flex;align-items:center;gap:14px;top:32px}
.ring{width:44px;height:44px;border:2px solid var(--orange);border-radius:50%;display:flex;align-items:center;justify-content:center}
.contact small{display:block;color:var(--orange);font-size:15px}
.contact b{display:block;color:var(--ink);font-size:19px;font-weight:500}
.nav{top:107px;left:0;width:1200px;height:43px;background:var(--orange);display:flex;align-items:center;padding-left:84px;gap:32px}
.nav a{color:var(--white);font-size:13.5px;font-weight:700;text-decoration:none}
.nav a.active{color:var(--ink)}

/* hero */
.hero{top:150px;left:0;width:1200px;height:563px;background:linear-gradient(100deg,#d9d4cd 0%,#bdb6ad 45%,#8c8075 70%,#a89e94 100%)}
.hero h1{position:absolute;top:170px;width:100%;text-align:center;font-size:42px;color:var(--white)}
.hero p{position:absolute;top:238px;width:100%;text-align:center;color:var(--white);font-size:17.5px;line-height:30px}
.btn{display:inline-block;background:var(--orange);color:var(--white);font-weight:700;font-size:17px;border-radius:26px;text-align:center}
.hero .btn{position:absolute;left:505px;top:328px;width:192px;height:50px;line-height:50px}

/* services */
.section-title{position:absolute;width:100%;text-align:center;font-size:34px}
.card{width:334px;height:286px}
.card .pic{height:228px}
.card .label{height:58px;background:var(--orange);color:var(--white);font-size:22px;font-weight:500;text-align:center;line-height:58px}

/* about */
.about-photo{top:1532px;left:0;width:600px;height:590px;background:linear-gradient(160deg,#c9cbcb,#7e8589 60%,#3d4347)}
.about-panel{top:1532px;left:600px;width:600px;height:590px;background:var(--orange)}
.bubble{width:80px;height:80px;border-radius:50%;background:var(--white);border:3px solid var(--orange);left:560px;display:flex;align-items:center;justify-content:center;box-shadow:0 0 0 3px var(--white)}
.about-text{left:684px;top:1610px;width:460px;color:var(--white)}
.about-text h2{font-size:35px;color:var(--white);margin-bottom:22px}
.about-text .lead{font-weight:700;font-size:15.5px;line-height:27px}
.about-text .body{font-size:15.5px;line-height:27px;margin-top:8px}
.about-text ul{list-style:none;margin-top:14px}
.about-text li{font-size:14px;line-height:27px;padding-left:36px;position:relative}
.about-text li:before{content:"»";position:absolute;left:0}
.about-text .btn{background:var(--white);color:var(--orange);font-weight:500;font-size:16px;width:143px;height:46px;line-height:46px;margin-top:24px}

/* testimonials */
.avatar{border-radius:50%;background:linear-gradient(145deg,#d8c3b5,#8a6a5a);border:3px solid #ddd}
.quote-name{top:2404px;width:100%;text-align:center;font-size:18px;font-weight:500;color:var(--ink)}
.stars{top:2432px;width:100%;text-align:center}
.quote{top:2464px;left:140px;width:920px;text-align:center;font-size:15px;line-height:27px}
.origin{top:2532px;width:100%;text-align:center;font-size:14px;font-style:italic;font-weight:500}

/* gallery */
.gallery{top:2636px;left:0;width:1200px;height:659px;background:var(--light)}
.tile{width:300px;height:212px}

/* footer */
.footer{top:3295px;left:0;width:1200px;height:378px;background:var(--footer);color:var(--white)}
.footer h4{font-size:21px;font-weight:500;position:absolute;top:70px}
.footer ul{list-style:none;position:absolute;top:110px}
.footer li{font-size:13px;line-height:27px}
.social{left:98px;top:190px;display:flex;gap:24px}
.social span{width:16px;height:16px;background:var(--white);border-radius:3px}
.copy{top:343px;width:100%;text-align:center;font-size:13px}
</style>
</head>
<body>

<header class="abs header">
  <div class="abs brand"><span class="brand-mark"></span><span class="brand-name">Keystone Recovery<br>Services</span></div>
  <div class="abs contact" style="left:525px">
    <span class="ring"><svg width="18" height="18" viewBox="0 0 24 24"><path fill="#f37321" d="M6.6 10.8a15.1 15.1 0 0 0 6.6 6.6l2.2-2.2a1 1 0 0 1 1-.25 11.4 11.4 0 0 0 3.6.57 1 1 0 0 1 1 1V20a1 1 0 0 1-1 1A17 17 0 0 1 3 4a1 1 0 0 1 1-1h3.5a1 1 0 0 1 1 1c0 1.25.2 2.45.57 3.57a1 1 0 0 1-.25 1z"/></svg></span>
    <div><small>Call Us :</small><b>0400 123 456</b></div>
  </div>
  <div class="abs contact" style="left:785px">
    <span class="ring"><svg width="20" height="16" viewBox="0 0 20 16"><rect width="20" height="16" rx="2" fill="#f37321"/><path d="M1 2l9 7 9-7" stroke="#fff" stroke-width="1.8" fill="none"/></svg></span>
    <div><small>Email :</small><b>info@mysite.com</b></div>
  </div>
  <div class="abs ring" style="left:1062px;top:32px"><svg width="16" height="16" viewBox="0 0 16 16"><circle cx="6.5" cy="6.5" r="5" stroke="#f37321" stroke-width="2" fill="none"/><path d="M10.5 10.5L15 15" stroke="#f37321" stroke-width="2"/></svg></div>
</header>

<nav class="abs nav">
  <a class="active">Home</a><a>Fire &amp; Smoke Restoration</a><a>Water Restoration</a><a>Mould Remediation</a><a>Crime Scene Cleaners</a><a>Methamphetamine Remediation</a><a>More ⌄</a>
</nav>

<section class="abs hero" role="img" aria-label="Smiling cleaner wiping a glass door">
  <h1 class="display">KEYSTONE RECOVERY SERVICES</h1>
  <p>Lorem ipsum dolor sit amet, consectetur adipiscing elit, sed do eiusmod tempor incididunt ut labore et dolore<br>Ut enim ad minim veniam, quis nostrud exercitation ullamco laboris nisi ut aliquip ex</p>
  <span class="btn">Get Started</span>
</section>

<h2 class="display section-title" style="top:795px">SERVICES</h2>
<div class="abs card" style="left:90px;top:854px"><div class="pic" role="img" aria-label="Mop cleaning tiled floor" style="background:linear-gradient(135deg,#ddd,#888)"></div><div class="label">Bond Cleaning</div></div>
<div class="abs card" style="left:433px;top:854px"><div class="pic" role="img" aria-label="Colourful spray bottles" style="background:linear-gradient(135deg,#e8e8e8,#b8c94a 50%,#d44)"></div><div class="label">Spring Cleaning</div></div>
<div class="abs card" style="left:777px;top:854px"><div class="pic" role="img" aria-label="Gloved hand cleaning a window" style="background:linear-gradient(135deg,#cfd8de,#e5d43c 50%,#2a8fc9)"></div><div class="label">Window Cleaning</div></div>
<div class="abs card" style="left:90px;top:1156px"><div class="pic" role="img" aria-label="Carpet steam cleaning machine in hallway" style="background:linear-gradient(135deg,#6b5e50,#b0aca6 55%,#4a4540)"></div><div class="label">Carpet Steam Cleaning</div></div>
<div class="abs card" style="left:433px;top:1156px"><div class="pic" role="img" aria-label="Floor polishing machine in office" style="background:linear-gradient(180deg,#d8dfe3,#a9b3ba)"></div><div class="label">Commercial Cleaning</div></div>
<div class="abs card" style="left:777px;top:1156px"><div class="pic" role="img" aria-label="Gloved hands scrubbing a granite surface" style="background:linear-gradient(135deg,#9a9a9a,#d4d4d4 50%,#e8d33a)"></div><div class="label">Crime &amp; Trauma Scene Cleaning</div></div>

<div class="abs about-photo" role="img" aria-label="Cleaner mopping an office corridor floor"></div>
<div class="abs about-panel"></div>
<div class="abs bubble" style="top:1580px"><svg width="36" height="36" viewBox="0 0 36 36" fill="none" stroke="#f37321" stroke-width="2"><rect x="4" y="6" width="28" height="24" rx="2"/><path d="M8 24l7-7 5 4 9-10"/></svg></div>
<div class="abs bubble" style="top:1684px"><svg width="36" height="36" viewBox="0 0 36 36" fill="none" stroke="#f37321" stroke-width="2"><rect x="8" y="5" width="20" height="27" rx="2"/><path d="M12 13h12M12 18h12M12 23h8"/></svg></div>
<div class="abs bubble" style="top:1787px"><svg width="36" height="36" viewBox="0 0 36 36" fill="none" stroke="#f37321" stroke-width="2"><circle cx="18" cy="18" r="13"/><path d="M12 18l4 4 8-8"/></svg></div>
<div class="abs bubble" style="top:1891px"><svg width="36" height="36" viewBox="0 0 36 36" fill="none" stroke="#f37321" stroke-width="2"><circle cx="18" cy="18" r="6"/><circle cx="18" cy="18" r="13" stroke-dasharray="4 3"/></svg></div>
<div class="abs bubble" style="top:1995px"><svg width="36" height="36" viewBox="0 0 36 36" fill="none" stroke="#f37321" stroke-width="2"><circle cx="20" cy="14" r="9"/><path d="M20 9v10M17 11h5a2 2 0 0 1 0 4h-4a2 2 0 0 0 0 4h5M5 30l6-6h8"/></svg></div>
<div class="abs about-text">
  <h2 class="display">ABOUT US</h2>
  <p class="lead">Rowan Ellery specialises in all Forensic &amp; Trauma Cleaning, Domestic and Commercial cleaning. Rowan Ellery services the Southest QLD Region.</p>
  <p class="body">Rowan Ellery has a team of experienced and quality driven cleaners, we pride ourselves on:</p>
  <ul>
    <li>Providing The Best Clean</li>
    <li>Attention To Detail</li>
    <li>Customer Satisfaction</li>
    <li>Friendly Service And Listening To The Needs Of Our Customers</li>
    <li>A Competitive Price For The Best Quality Service</li>
  </ul>
  <span class="btn">Read More</span>
</div>

<h2 class="display section-title" style="top:2203px">TESTIMONIALS</h2>
<div class="abs avatar" role="img" aria-label="Customer portrait" style="left:373px;top:2280px;width:94px;height:94px"></div>
<div class="abs avatar" role="img" aria-label="Customer portrait" style="left:542px;top:2269px;width:116px;height:116px;background:linear-gradient(145deg,#e6e6e6,#9a8676)"></div>
<div class="abs avatar" role="img" aria-label="Customer portrait" style="left:733px;top:2280px;width:94px;height:94px;background:linear-gradient(145deg,#c9b2a2,#5c4234)"></div>
<div class="abs quote-name">Lena Marsh</div>
<div class="abs stars"><svg width="136" height="16" viewBox="0 0 136 16" fill="#f5a623"><g id="st"><path d="M8 0l2.4 5.2 5.6.6-4.2 3.8 1.2 5.6L8 12.4 3 15.2l1.2-5.6L0 5.8l5.6-.6z"/></g><use href="#st" x="30"/><use href="#st" x="60"/><use href="#st" x="90"/><use href="#st" x="120"/></svg></div>
<p class="abs quote">Lorem ipsum dolor sit amet, consectetur adipiscing elit, sed do eiusmod tempor incididunt ut labore et dolore magna aliqua. Ut enim ad minim veniam, quis nostrud exercitation ullamco laboris nisi ut aliquip ex ea commodo consequat.</p>
<div class="abs origin">- USA</div>

<section class="abs gallery">
  <h2 class="display section-title" style="top:84px">PROJECT GALLERY</h2>
  <div class="abs tile" role="img" aria-label="Cluttered room with cleaning containers" style="left:145px;top:143px;background:linear-gradient(135deg,#5a4030,#b59a3a 50%,#3b3b4a)"></div>
  <div class="abs tile" role="img" aria-label="Room before and after clearing" style="left:450px;top:143px;background:linear-gradient(180deg,#3d3535 0%,#6a5a58 48%,#e8e8e8 52%,#bbb 100%)"></div>
  <div class="abs tile" role="img" aria-label="Technician in protective suit removing carpet" style="left:755px;top:143px;background:linear-gradient(135deg,#c9a64a,#e9e4d8 50%,#6b3d20)"></div>
  <div class="abs tile" role="img" aria-label="Hoarded garage full of items" style="left:145px;top:358px;background:linear-gradient(135deg,#4a5260,#a8613a 50%,#5b6f8a)"></div>
  <div class="abs tile" role="img" aria-label="Trailer on grass under trees" style="left:450px;top:358px;background:linear-gradient(180deg,#5b8fd8 0%,#6a8a4a 55%,#8aa04a 100%)"></div>
  <div class="abs tile" role="img" aria-label="Trailer loaded with green waste" style="left:755px;top:358px;background:linear-gradient(180deg,#7fa0c0 0%,#5a6a48 45%,#8a8a88 100%)"></div>
</section>

<footer class="abs footer">
  <div class="abs brand" style="left:90px;top:80px"><span class="brand-mark"></span><span class="brand-name">Keystone Recovery<br>Services</span></div>
  <div class="abs social"><span></span><span></span><span></span><span></span><span></span></div>
  <h4 style="left:400px">Links</h4>
  <ul style="left:400px"><li>Home</li><li>Fire &amp; Smoke Restoration</li><li>Water Restoration</li><li>Mould Remediation</li><li>Crime Scene Cleaners</li></ul>
  <ul style="left:663px"><li>Methamphetamine Remediation</li><li>Hoarding &amp; Squalor Cleaning,</li><li>Contact Us</li><li>Testimonials</li></ul>
  <h4 style="left:960px">Others</h4>
  <ul style="left:960px"><li>FAQ</li><li>Privacy Policy</li><li>Terms &amp; Conditions</li></ul>
  <div class="abs copy">Copyright © 2020.The Company Name. All Rights Reserved.</div>
</footer>

</body>
</html>
```